Business Card Design Project

Hi,

We are a new modern sheet metal business and I require a business card for our sales reps.

The card should be double sided and standout in a crowd.

I have attached our logo and our website is www.ostrakan.com.au.

Please ask if you have any further questions
Updates

hi everyone, 

I'm wondering if we can try to lighten the cards mood.  Everyone is using black and I'm not sure how that would be accepted in real life.

Gordon

Reason: Still No receiving what I was hoping for.

Industry/Entity Type

Business

Requirements
Must have
• double sided

```html
<!DOCTYPE html>
<html lang="en">
<head>
<meta charset="utf-8">
<title>Ostrakan Sheetmetal – Business Card</title>
<link rel="stylesheet" href="https://fonts.googleapis.com/css2?family=Open+Sans:wght@400;600;700&display=swap">
<style>
  :root {
    --backdrop: #4b4b4b;
    --metal-light: #e2e2e2;
    --metal-mid: #cfcfcf;
    --metal-dark: #bdbdbd;
    --navy: #1c2f7a;
    --ink: #2b2b2b;
    --muted: #4a4a4a;
  }
  * { box-sizing: border-box; margin: 0; padding: 0; }
  html, body {
    width: 1200px; height: 1000px; overflow: hidden;
    background: var(--backdrop);
    font-family: "Open Sans", Arial, sans-serif;
  }
  .canvas { position: relative; width: 1200px; height: 1000px; }
  .card {
    position: absolute; width: 528px; height: 300px;
    border-radius: 14px;
    background: linear-gradient(180deg, var(--metal-light) 0%, var(--metal-mid) 55%, var(--metal-dark) 100%);
  }
  .card--front { left: 207px; top: 165px; }
  .card--back { left: 473px; top: 551px; }

  /* Front */
  .brand {
    position: absolute; left: 0; right: 0; top: 92px;
    display: flex; align-items: center; justify-content: center; gap: 12px;
    color: var(--navy); font-weight: 700;
  }
  .brand__square { width: 40px; height: 40px; background: var(--navy); flex: none; }
  .brand__name { font-size: 36px; line-height: 1; letter-spacing: 0.5px; }
  .brand__sub { display: block; font-size: 16px; letter-spacing: 6.5px; margin-top: 8px; }
  .services {
    position: absolute; left: 0; right: 0; top: 208px;
    text-align: center; font-size: 12.5px; color: var(--muted);
  }
  .services__sep { display: inline-block; width: 2px; height: 13px; background: var(--navy); margin: 0 5px; vertical-align: -2px; }
  .website {
    position: absolute; left: 0; right: 0; top: 252px;
    text-align: center; font-size: 15px; color: var(--ink);
  }
  .website strong { color: var(--navy); font-weight: 700; }

  /* Back */
  .person { position: absolute; right: 310px; top: 118px; text-align: right; }
  .person__name { font-size: 23px; font-weight: 700; color: var(--navy); letter-spacing: 0.3px; }
  .person__role { font-size: 14px; color: var(--ink); margin-top: 6px; }
  .divider { position: absolute; left: 262px; top: 99px; width: 1.5px; height: 101px; background: #444; }
  .contact {
    position: absolute; left: 307px; top: 103px;
    font-size: 15px; line-height: 23.5px; color: var(--ink);
  }
  .contact__row { display: flex; align-items: center; }
  .contact__icon { width: 18px; margin-right: 9px; display: flex; justify-content: flex-start; }
</style>
</head>
<body>
<main class="canvas">
  <section class="card card--front" aria-label="Card front">
    <div class="brand">
      <span class="brand__square"></span>
      <span class="brand__name">OSTRAKAN<span class="brand__sub">SHEETMETAL</span></span>
    </div>
    <p class="services">Flashings<span class="services__sep"></span>Gutter<span class="services__sep"></span>Rainwater Goods</p>
    <p class="website">www.<strong>ostrakan</strong>.com.au</p>
  </section>

  <section class="card card--back" aria-label="Card back">
    <div class="person">
      <p class="person__name">LIAM CARTER</p>
      <p class="person__role">Sales Manager</p>
    </div>
    <div class="divider"></div>
    <div class="contact">
      <p>27 Harbour Road</p>
      <p>Kiama NSW 2533</p>
      <p class="contact__row">
        <span class="contact__icon">
          <svg width="10" height="16" viewBox="0 0 10 16" aria-hidden="true">
            <rect x="1" y="1" width="8" height="14" rx="1.5" fill="none" stroke="var(--navy)" stroke-width="1.8"/>
            <rect x="4" y="12" width="2" height="1.5" fill="var(--navy)"/>
          </svg>
        </span>0400 123 456
      </p>
      <p class="contact__row">
        <span class="contact__icon">
          <svg width="16" height="11" viewBox="0 0 16 11" aria-hidden="true">
            <rect x="0.5" y="0.5" width="15" height="10" fill="var(--navy)"/>
            <path d="M1 1 L8 6.5 L15 1" fill="none" stroke="var(--metal-light)" stroke-width="1.2"/>
          </svg>
        </span>info@ostrakan.com.au
      </p>
    </div>
  </section>
</main>
</body>
</html>
```